依頼概要
初めまして。本書は、会社等の会議を実施する立場の人に向けてのものと
なっております。
■依頼の目的/概要
lumora出版、ビジネスパーソン向け書籍の表紙デザインをお願いします。
今のところ、題名は
「だれでも週末から家庭菜園がはかどる」

■本の内容
会社等で、会議をうまく進めていきたいがなかなか思うように
薦められない方向けに、誰でも簡単にこれだけのことを実践すれば
会議が上手く進められるというポイントをまとめたものになっております。

■デザイン要望
ビジネスパーソン向けですが、会議等に不慣れな方向けで
あまり難しく考えなくても、誰でも簡単にトライできるという
イメージを持ってもらえるようにしたいです。

現在、原稿は9割がたできております。添付ファイルをご参照ください。

その他何かご不明な点がございましたら、お気軽にご質問下さい。
よろしくお願いいたします。
名前は、ペンネームにする予定です。
今のところ、柚木 瑛之助が候補です。
■ 選んだ理由

私のイメージする会社内での和気あいあいとした雰囲気のイラストがまずは
気に入りました。
ターゲットが、会議がうまくできない人向けなので、なるべくそれを意識して
親しみやすいものを選びました。

■ 提案者全員のお礼・コメント

今回は、ターゲットが初心者向けであったので、親しみやすいものを選びましたが、
例えば、会議を上から見たイラストなどは、斬新なアイデアで印象深く
ターゲットが違えば、選んでいたと思います。
中身を理解して、提案いただけた方も多く、感謝いたします。
今後も、このシリーズを出版していきたいと考えておりますので
次の機会もよろしくお願いいたします。
ありがとうございました。

```html
<!DOCTYPE html>
<html lang="ja">
<head>
<meta charset="UTF-8">
<title>だれでも週末から家庭菜園がはかどる</title>
<link href="https://fonts.googleapis.com/css2?family=Noto+Sans+JP:wght@500;700;900&family=Noto+Serif+JP:wght@700&display=swap" rel="stylesheet">
<style>
  :root {
    --blue: #1461c4;
    --red: #d0182f;
    --navy: #1c2f6a;
    --yellow: #ffe300;
    --ink: #2a2a2a;
    --paper: #ffffff;
  }
  html, body { margin: 0; padding: 0; overflow: hidden; }
  body { width: 750px; height: 1200px; background: var(--paper); font-family: "Noto Sans JP", sans-serif; }
  .cover { position: relative; width: 750px; height: 1200px; overflow: hidden; background: var(--paper); }
  .vertical { position: absolute; writing-mode: vertical-rl; text-orientation: upright; margin: 0; line-height: 1; white-space: nowrap; z-index: 2; }

  .ribbon { position: absolute; left: 568px; top: 0; width: 104px; height: 430px; }
  .ribbon-text { left: 585px; top: 40px; font-size: 70px; font-weight: 900; color: var(--paper); letter-spacing: 4px; }

  .title-line { color: var(--blue); font-weight: 900; }
  .line-when { left: 470px; top: 150px; font-size: 72px; letter-spacing: 2px; }
  .line-act { left: 172px; top: 120px; font-size: 70px; letter-spacing: 4px; }

  .title-main { position: absolute; left: 278px; top: 60px; width: 120px; display: flex; flex-direction: column; align-items: center; z-index: 2; }
  .title-main .big { writing-mode: vertical-rl; text-orientation: upright; font-size: 108px; font-weight: 900; color: var(--blue); line-height: 1; }
  .title-main .reading { margin: 6px 0; background: var(--blue); color: var(--paper); font-size: 15px; font-weight: 700; letter-spacing: 1px; padding: 2px 6px; white-space: nowrap; }

  .bubble { position: absolute; left: 352px; top: 528px; width: 92px; height: 72px; z-index: 2; }
  .bubble-text { position: absolute; left: 368px; top: 536px; width: 62px; text-align: center; font-size: 52px; font-weight: 900; color: var(--blue); line-height: 1; z-index: 3; }

  .author { left: 70px; top: 385px; font-family: "Noto Serif JP", serif; font-weight: 700; font-size: 36px; color: var(--ink); letter-spacing: 2px; }

  .people-art { position: absolute; left: 0; top: 636px; width: 750px; height: 176px; background: linear-gradient(180deg, #ffffff 0%, #e7eef8 55%, #c9d8ee 100%); z-index: 1; }

  .band { position: absolute; left: 0; top: 812px; width: 750px; height: 388px; background: var(--navy); }
  .lead { position: absolute; left: 0; width: 750px; text-align: center; margin: 0; white-space: nowrap; }
  .lead-1 { top: 840px; font-size: 42px; font-weight: 900; color: var(--paper); }
  .lead-2 { top: 912px; font-size: 53px; font-weight: 900; color: var(--yellow); }
  .note { position: absolute; left: 150px; top: 1012px; width: 580px; height: 150px; background: var(--paper); padding: 18px 22px; box-sizing: border-box; }
  .note p { margin: 0; font-size: 26px; font-weight: 700; color: var(--ink); line-height: 1.45; }
  .note .note-strong { margin-top: 12px; color: var(--blue); font-size: 31px; font-weight: 900; }
</style>
</head>
<body>
<main class="cover">
  <svg class="ribbon" viewBox="0 0 104 430" aria-hidden="true">
    <polygon points="0,0 104,0 104,430 52,392 0,430" fill="var(--red)"/>
  </svg>
  <h1 class="vertical ribbon-text">だれでも</h1>

  <p class="vertical title-line line-when">週末から</p>

  <div class="title-main">
    <span class="big">家庭</span>
    <span class="reading">KATEI SAIEN</span>
    <span class="big">菜園</span>
  </div>

  <svg class="bubble" viewBox="0 0 92 72" aria-hidden="true">
    <path d="M18,10 L4,2 L22,18 A32,32 0 1 0 30,10 Z" fill="var(--paper)" stroke="var(--blue)" stroke-width="4"/>
  </svg>
  <span class="bubble-text">が</span>

  <p class="vertical title-line line-act">はかどる</p>

  <p class="vertical author">柚木　瑛之助</p>

  <div class="people-art" role="img" aria-label="笑顔で指を立てる会社員たちのイラスト"></div>

  <section class="band"></section>
  <p class="lead lead-1">これだけ準備しておけば大丈夫!</p>
  <p class="lead lead-2">アジェンダと終了条件だけ。</p>
  <div class="note">
    <p>「会議をもっとうまく進められたらー」と<br>悩んでいる”あなた”へ。</p>
    <p class="note-strong">すぐに使える小ネタを集約!!</p>
  </div>
</main>
</body>
</html>
```